New Website for QWRB Holdings (Property Leasing Company in New Haven)

Design a fully functioning website for a real estate property leasing company. The company has a few properties in New Haven, CT and would like to provide an option for its tenants to pay their rent online. The company should have the ability to generate unique account log in username and password for its tenants so they can make online payments through ACH the website. (The ACH processing part will be coordinated with the bank).

Please take a look at all the pictures I uploaded of New Haven especially the area around Marlow College, you will find that the general style is Gothic and charming.

Also please make use of the pictures of the two properties I have attached to the description.

Please keep Holdings page, Contact Us Page , About Us Page, and please add a page entitled "Tenants".

On the Holdings page I would like to see on the left hand side an interactive map of new haven (Please see a map attached), split by New Haven's neighbourhoods, and showing my properties as pins of sort on the map (I can send you the addresses of the properties upon request). On the same page on the right side I want to see a drop down menu that includes list of New Haven Neighbourhoods. When a neighbourhood is selected you can see in the space underneath the drop-down menu the properties we have in that neighbourhood in large thumbnail format. Also on the map you can see the pins corresponding to those properties change colour. A user can either click on the pin or on the thumbnails to have view more pictures of the property and some details in text.

The tenants page should prompt a login to access- I like your idea of having the company name in two colours, one for QWRB and another for Holdings.Please let me know if you have any questions along the way

-------------------------------------------------------------------------------
Property Descriptions for Holdings Page
The Larch Lodge,

Neighbourhood: Westville
Name: Silas Brennaway House
Building Style: Queen Anne Style
Address: 418 Pellwin Road, New Haven, CT 06515
Number of Units: 3
Unit Names: Unit 1, Unit 2, Unit 3

Property Description

This Westiville home was built in 1897, historically known as The Silas Brennaway House, it is an example of the Queen Anne style. The large carriage house is still intact and sits in the lovely, expansive back garden! An outstanding architectural feature of the house is the turret, giving the home prominence on Pellwin Road. This well maintained home has renovated kitchens in all units, the first floor has granite and red oak cabinetry. New baths and central air in all apartments. All newer mechanicals for each unit, all natural gas. The entire house has replacement windows. The new back deck overlooks the back garden and carriage house. The front steps and porch have also been rebuilt. Roof has 30 year architectural singles and approximately 15 years old, the chimney has just been lined.

Unit 1 Description:

2 Bedrooms, 6 rooms in total.
Amenities: Dishwasher, Central Air, Gas Heating, Porch

Unit 2 Description:

2 Bedrooms, 5 rooms in total.
Amenities: Dishwasher, Central Air, Gas Heating, Balcony

Unit 3 Description:

2 Bedrooms, 4 rooms in total.
Amenities: Dishwasher, Central Air, Gas Heating

The Fern Lodge:

Neighbourhood: East Rock
Name: 64 Birchmere
Building Style: Victorian
Address: 64 Birchmere Lane, New Haven, CT 06511
Number of Units: 2
Unit Names: Unit 1, and Unit 2

Property Description

East Rock incredibly charming newly renovated 2 family on quiet tree-lined block. Tenants are responsible for all utilities (gas heat, electricity and cable). Small pets are possible with landlord approval. Tenants has use of shared yard, laundry in the basement and on street parking only. Located steps away from gourmet markets & minutes to Downtown New Haven, Marlow & local hospitals. Fascinating backyard. This is a feel good house!

Unit 1 Description:

Area:
1100 soft, 3 Bedrooms, 5 rooms in total.
Amenities: In unit Washer and Dryer, Central Air, Gas Heating, Porch, Backyard

Unit 2 Description:

Area: 2,820 sqft
5 Bedrooms, 8 rooms in total.
Amenities: In unit Washer and Dryer, Dishwasher, Central Air, and Gas Heating

Target Market(s)

1-3 bedroom Renting Market around Marlow College and New Haven Community

Industry/Entity Type

Real Estate

Coding

Coded - Design and coding required

Number of Pages Required

4 page

Font styles to use
Other font styles liked:
• Helvetica

Colors
85cae6
cee9f5
d9d9d9
9d9d9d

Requirements
Must have
• Payment page with login (accounts can only be created by administrator)
• A page showcasing the properties (Professional photos to be uploaded shortly)
• A page for technical support, contact information and so forth
• Home page
Nice to have
• A professional, but stylish design. Not too colourful, something with pastel colours
Should not have
• A lot of colours, any pop-ups,

```html
<!DOCTYPE html>
<html lang="en">
<head>
<meta charset="utf-8">
<title>QWRB Holdings</title>
<link href="https://fonts.googleapis.com/css2?family=Open+Sans:wght@400;600;700&family=Oswald:wght@500;600&display=swap" rel="stylesheet">
<style>
:root{
  --sky:#85cae6;
  --sky-pale:#cee9f5;
  --grey-light:#d9d9d9;
  --grey-mid:#9d9d9d;
  --blue:#1f6fa8;
  --blue-deep:#1b5f91;
  --ink:#333;
  --band:#e8f1f6;
  --partners:#efefef;
  --footer:#585858;
  --footer-base:#444;
  --white:#fff;
}
*{box-sizing:border-box;margin:0;padding:0}
html,body{width:1200px;height:2944px;overflow:hidden}
body{font-family:"Open Sans",Arial,sans-serif;color:var(--ink);background:var(--white);position:relative}
.section{position:absolute;left:0;width:1200px}
.title{font-size:34px;font-weight:700;color:var(--blue-deep);display:flex;align-items:center;justify-content:center;gap:22px}
.title::before,.title::after{content:"";width:330px;height:1px;background:var(--grey-light)}
.title .accent{color:var(--sky)}
.btn{display:inline-block;background:var(--blue);color:var(--white);font-weight:600;font-size:15px;padding:10px 26px;border-radius:3px}
.photo{border-radius:2px}

/* header */
.header{top:0;height:112px;background:var(--white)}
.logo{position:absolute;left:80px;top:16px;display:flex;align-items:center;gap:12px}
.logo-mark{width:34px;height:34px;background:var(--sky)}
.logo-name{font-size:30px;font-weight:700;line-height:32px;color:var(--sky)}
.contact-top{position:absolute;right:84px;top:14px;display:flex;align-items:center;gap:20px;font-size:20px;color:var(--blue-deep)}
.contact-top .phone{display:flex;align-items:center;gap:8px}
.login{background:var(--blue);color:var(--white);font-size:14px;font-weight:600;padding:8px 24px;border-radius:3px}
.nav{position:absolute;right:84px;top:74px;display:flex;gap:40px;font-size:17px;color:#555}

/* hero */
.hero{top:112px;height:576px;background:
  radial-gradient(ellipse 260px 320px at 50% 78%,rgba(150,72,52,.95),rgba(150,72,52,0) 70%),
  radial-gradient(ellipse 90px 120px at 36% 30%,rgba(138,70,52,.9),rgba(138,70,52,0) 75%),
  radial-gradient(ellipse 90px 120px at 64% 30%,rgba(138,70,52,.9),rgba(138,70,52,0) 75%),
  radial-gradient(ellipse 300px 420px at 8% 45%,rgba(176,150,54,.95),rgba(110,118,46,0) 75%),
  radial-gradient(ellipse 300px 420px at 94% 50%,rgba(154,162,58,.95),rgba(96,118,44,0) 75%),
  radial-gradient(ellipse 700px 160px at 50% 100%,rgba(70,96,44,.9),rgba(70,96,44,0) 80%),
  linear-gradient(180deg,#9fc2df 0%,#c9dde9 45%,#b8b6a2 70%,#6f7e4a 100%)}
.hero::after{content:"";position:absolute;inset:0;background:linear-gradient(180deg,rgba(0,0,0,0) 30%,rgba(0,0,0,.18) 55%,rgba(0,0,0,0) 80%)}
.hero h1{position:absolute;z-index:1;top:250px;width:100%;text-align:center;font-family:"Oswald",Impact,sans-serif;font-weight:600;font-size:46px;color:var(--white);letter-spacing:1px;text-shadow:0 2px 6px rgba(0,0,0,.35)}
.hero .btn{position:absolute;z-index:1;top:340px;left:525px;font-size:14px}

/* search */
.finder{top:688px;height:224px;background:var(--sky-pale)}
.finder h2{position:absolute;left:80px;top:38px;font-size:26px;font-weight:700;color:var(--blue-deep);display:flex;align-items:center;gap:12px}
.fields{position:absolute;left:80px;top:92px;width:1040px;display:grid;grid-template-columns:repeat(4,1fr);gap:18px 22px}
.field{height:38px;background:var(--white);border:1px solid var(--grey-light);font-size:12px;color:#777;display:flex;align-items:center;justify-content:space-between;padding:0 12px;text-transform:uppercase}
.field::after{content:"";border:5px solid transparent;border-top-color:var(--grey-mid);margin-top:5px}
.row2-wrap{grid-column:1/-1;display:grid;grid-template-columns:repeat(3,1fr) 0.6fr 0.5fr;gap:22px}
.search{background:var(--blue);color:var(--white);font-weight:700;font-size:14px;display:flex;align-items:center;justify-content:center;height:38px}

/* popular */
.popular{top:912px;height:560px}
.popular .title{position:absolute;top:44px;width:100%}
.cards{position:absolute;left:80px;top:116px;width:1040px;display:flex;justify-content:space-between}
.card{width:324px;text-align:center}
.card .photo{height:264px}
.card p{margin-top:30px;font-size:14px;font-weight:700;color:#444}
.popular .btn{position:absolute;top:464px;left:525px;background:var(--white);color:#555;border:1px solid var(--grey-mid);font-size:13px}

/* agents */
.agents{top:1472px;height:456px;background:var(--band)}
.agents .title{position:absolute;top:40px;width:100%}
.agent-row{position:absolute;left:80px;top:108px;width:1040px;display:flex;justify-content:space-between}
.agent{width:230px;text-align:center}
.agent .avatar{width:200px;height:200px;border-radius:50%;margin:0 auto;border:6px solid var(--white);box-shadow:0 2px 6px rgba(0,0,0,.12)}
.agent h3{margin-top:30px;font-size:21px;font-weight:600;color:var(--blue-deep);letter-spacing:1px}
.agent p{font-size:13px;color:#555;margin-top:10px}

/* gallery */
.gallery{top:1928px;height:372px}
.gallery .title{position:absolute;top:72px;width:100%}
.g-row{position:absolute;left:80px;top:142px;width:1040px;display:flex;justify-content:space-between}
.g-item{width:236px;text-align:center}
.g-item .photo{height:156px;position:relative}
.g-item .overlay{position:absolute;left:0;top:0;right:0;bottom:0;padding:18px 14px;text-align:left;color:var(--white);font-size:12px;line-height:15px;background:rgba(30,40,50,.45)}
.g-item .overlay b{display:block;font-size:13px}
.g-item p{margin-top:14px;font-size:13px;font-weight:700;color:#444}

/* partners */
.partners{top:2300px;height:232px;background:var(--partners)}
.partners .title{position:absolute;top:52px;width:100%}
.partners .title::before,.partners .title::after{width:350px}
.logos{position:absolute;left:80px;top:134px;width:1040px;display:flex;align-items:center;justify-content:space-between}
.arrow{color:var(--grey-mid);font-size:30px}
.partner{display:flex;align-items:center;gap:8px;font-size:22px;font-weight:700;color:#444}
.partner i{width:18px;height:18px;border-radius:50%;background:var(--grey-mid);display:block}

/* footer */
.footer{top:2532px;height:356px;background:var(--footer);color:var(--white)}
.col{position:absolute;top:40px}
.col h4{font-size:26px;font-weight:600;letter-spacing:1px;margin-bottom:26px}
.col1{left:80px;width:330px}
.listing{display:flex;gap:18px;margin-bottom:22px}
.listing .thumb{width:96px;height:74px;flex:none}
.listing p{font-size:12px;line-height:16px;color:#ddd}
.listing b{color:var(--white);display:block;font-size:13px;margin-bottom:2px}
.col2{left:456px;width:280px}
.col2 .lead{font-size:13px;color:#ddd;margin-bottom:16px}
.input{height:40px;background:var(--white);color:#999;font-size:13px;display:flex;align-items:center;padding:0 12px;margin-bottom:14px}
.submit{height:40px;background:var(--sky);font-size:14px;font-weight:700;display:flex;align-items:center;justify-content:center}
.col3{left:830px;width:290px;font-size:13px;line-height:19px;color:#ddd}
.col3 p{margin-bottom:14px}
.col3 b{color:var(--white)}
.base{top:2888px;height:56px;background:var(--footer-base);color:#ccc;font-size:12px;display:flex;align-items:center;justify-content:space-between;padding:0 80px}
.social{display:flex;gap:10px}
.social i{width:26px;height:26px;border-radius:50%;background:var(--grey-mid);display:block}
</style>
</head>
<body>

<header class="section header">
  <div class="logo"><div class="logo-mark"></div><div class="logo-name">QWRB<br>Holdings</div></div>
  <div class="contact-top">
    <span class="phone"><svg width="18" height="18" viewBox="0 0 24 24"><path fill="#1f6fa8" d="M6.6 10.8a15 15 0 006.6 6.6l2.2-2.2a1 1 0 011-.3 11.4 11.4 0 003.6.6 1 1 0 011 1V20a1 1 0 01-1 1A17 17 0 013 4a1 1 0 011-1h3.5a1 1 0 011 1 11.4 11.4 0 00.6 3.6 1 1 0 01-.3 1z"/></svg>203 555 0100</span>
    <span class="login">LOGIN</span>
  </div>
  <nav class="nav"><span>Home</span><span>About Us</span><span>Holdings</span><span>Tenants</span><span>Services</span><span>Contact</span></nav>
</header>

<section class="section hero" role="img" aria-label="Gothic brick gateway with twin towers framed by autumn trees">
  <h1>SPECIALIZING IN FASTER LEASING</h1>
  <span class="btn">GET STARTED</span>
</section>

<section class="section finder">
  <h2><svg width="30" height="28" viewBox="0 0 30 28"><path fill="#1f6fa8" d="M15 2 2 13h4v13h7v-8h4v8h7V13h4z"/></svg>Find A Property</h2>
  <div class="fields">
    <div class="field">Location</div><div class="field">Status</div><div class="field">Type</div><div class="field">Bedrooms</div>
    <div class="row2-wrap">
      <div class="field">Bathrooms</div><div class="field">Min Price</div><div class="field">Max Price</div><div class="field">Property Type</div><div class="search">SEARCH</div>
    </div>
  </div>
</section>

<section class="section popular">
  <h2 class="title"><span>Most <span class="accent">Popular</span></span></h2>
  <div class="cards">
    <div class="card"><div class="photo" role="img" aria-label="Brick house with garden and trees" style="background:radial-gradient(ellipse 120px 110px at 45% 55%,rgba(140,90,70,.9),rgba(140,90,70,0) 75%),radial-gradient(ellipse 160px 140px at 15% 20%,rgba(120,150,90,.9),rgba(120,150,90,0) 75%),linear-gradient(180deg,#b7c9cf 0%,#7d9066 45%,#5b6a45 100%)"></div><p>CONSEQUTE LAROTE SMIT DOLLAR AMET</p></div>
    <div class="card"><div class="photo" role="img" aria-label="Red brick building under blue sky" style="background:radial-gradient(ellipse 170px 80px at 45% 52%,rgba(160,72,50,.95),rgba(160,72,50,0) 75%),radial-gradient(ellipse 90px 140px at 90% 55%,rgba(190,120,50,.9),rgba(190,120,50,0) 75%),linear-gradient(180deg,#8fbbe0 0%,#b9d3e8 30%,#9a5c48 55%,#6f8350 100%)"></div><p>CONSEQUTE LAROTE SMIT DOLLAR AMET</p></div>
    <div class="card"><div class="photo" role="img" aria-label="Campus lawn with autumn trees" style="background:radial-gradient(ellipse 150px 90px at 30% 30%,rgba(210,150,50,.9),rgba(210,150,50,0) 75%),radial-gradient(ellipse 200px 80px at 55% 80%,rgba(120,165,60,.95),rgba(120,165,60,0) 75%),linear-gradient(180deg,#c9a851 0%,#8fa044 50%,#5f7c33 100%)"></div><p>CONSEQUTE LAROTE SMIT DOLLAR AMET</p></div>
  </div>
  <span class="btn">LOAD MORE</span>
</section>

<section class="section agents">
  <h2 class="title"><span>Meet Our <span class="accent">Agents</span></span></h2>
  <div class="agent-row">
    <div class="agent"><div class="avatar" role="img" aria-label="Agent portrait" style="background:linear-gradient(180deg,#8fa3a8 0%,#b9c4c4 45%,#3d4550 75%,#2c323b 100%)"></div><h3>TAVIN ROSHE</h3><p>&#9742; +1 203 555 0147</p><p>&#9993; tavin@qwrbmail.com</p></div>
    <div class="agent"><div class="avatar" role="img" aria-label="Agent portrait" style="background:linear-gradient(180deg,#e8eef2 0%,#d8c7a2 45%,#2f3338 78%,#22262b 100%)"></div><h3>MIRA CASTELL</h3><p>&#9742; +1 203 555 0148</p><p>&#9993; mira@qwrbmail.com</p></div>
    <div class="agent"><div class="avatar" role="img" aria-label="Agent portrait" style="background:linear-gradient(180deg,#5b7fa8 0%,#c9a58e 45%,#2a2f3a 75%,#8a2b2b 100%)"></div><h3>DEON HARLOW</h3><p>&#9742; +1 203 555 0149</p><p>&#9993; deon@qwrbmail.com</p></div>
    <div class="agent"><div class="avatar" role="img" aria-label="Agent portrait" style="background:linear-gradient(180deg,#eef2f4 0%,#cfb6a0 45%,#3a3f4a 75%,#2a3040 100%)"></div><h3>TAVIN ROSHE</h3><p>&#9742; +1 203 555 0147</p><p>&#9993; tavin@qwrbmail.com</p></div>
  </div>
</section>

<section class="section gallery">
  <h2 class="title"><span>Property <span class="accent">Gallery</span></span></h2>
  <div class="g-row">
    <div class="g-item"><div class="photo" role="img" aria-label="Historic house exterior" style="background:linear-gradient(180deg,#9fb5c4,#6f7c70 55%,#4e5a48)"><div class="overlay"><b>Duis autem vel eum</b>Iriure dolor in hendrerit in vulputate velit esse molestie</div></div><p>CONSEQUTE LAROTE</p></div>
    <div class="g-item"><div class="photo" role="img" aria-label="Brick building with arches" style="background:radial-gradient(ellipse 110px 50px at 50% 55%,rgba(160,80,55,.95),rgba(160,80,55,0) 75%),linear-gradient(180deg,#9cc3e3,#b9a08a 45%,#6f7f4c)"></div><p>DOLLAR SMIT RODOS</p></div>
    <div class="g-item"><div class="photo" role="img" aria-label="Stone street facade" style="background:radial-gradient(ellipse 90px 70px at 30% 55%,rgba(150,110,90,.9),rgba(150,110,90,0) 75%),linear-gradient(180deg,#c7dcec,#a99a86 45%,#6d5d50)"></div><p>NOKDLSF DOOFFUY</p></div>
    <div class="g-item"><div class="photo" role="img" aria-label="Tower among autumn trees" style="background:radial-gradient(ellipse 60px 90px at 55% 40%,rgba(150,85,60,.9),rgba(150,85,60,0) 75%),radial-gradient(ellipse 90px 70px at 15% 70%,rgba(200,150,60,.9),rgba(200,150,60,0) 75%),linear-gradient(180deg,#a7c7e0,#a99158 50%,#6f7d3e)"></div><p>WOSTED DULLS</p></div>
  </div>
</section>

<section class="section partners">
  <h2 class="title"><span>Our <span class="accent">Partners</span></span></h2>
  <div class="logos">
    <span class="arrow">&lsaquo;</span>
    <span class="partner"><i></i>Calder</span>
    <span class="partner">Norvane</span>
    <span class="partner"><i></i>Halbrook</span>
    <span class="partner"><i></i>Petrova</span>
    <span class="partner"><i></i>Calder</span>
    <span class="partner">Linwell</span>
    <span class="arrow">&rsaquo;</span>
  </div>
</section>

<footer class="section footer">
  <div class="col col1">
    <h4>FEATURED LISTING</h4>
    <div class="listing"><div class="thumb" role="img" aria-label="Listing photo of a house" style="background:linear-gradient(180deg,#b9c8cf,#8c7a62 50%,#5d6e45)"></div><p><b>Duis autem vel eum</b>Iriure dolor in hendrerit in vulputate velit esse molestie consequat.</p></div>
    <div class="listing"><div class="thumb" role="img" aria-label="Listing photo of a garden" style="background:linear-gradient(180deg,#a8c08a,#7a9a52 50%,#56703a)"></div><p><b>Duis autem vel eum</b>Iriure dolor in hendrerit in vulputate velit esse molestie consequat.</p></div>
  </div>
  <div class="col col2">
    <h4>NEWSLETTER</h4>
    <p class="lead">Get Free Latest updates &amp; News!</p>
    <div class="input">Name</div>
    <div class="input">Email</div>
    <div class="submit">SUBMIT</div>
  </div>
  <div class="col col3">
    <h4>GET IN TOUCH</h4>
    <p>Suite 204, 418 Pellwin Road, Westville Office Plaza, New Haven, CT 06515</p>
    <p><b>PH:</b> (203) 555 0100<br><b>FAX:</b> (203) 555 0101</p>
    <p><b>EM:</b> info@qwrbmail.com</p>
  </div>
</footer>

<div class="section base">
  <span>&copy; Copyright QWRB Holdings 2016</span>
  <div class="social"><i></i><i></i><i></i><i></i></div>
</div>

</body>
</html>
```